Private Label Design for Sparkling Wine for hotel

Our wine supplier has agree to allow us to private label a sparkling wine...but we have to provide them with the design. We would incorporate one of these two logos but I need fun design ideas too. Our hotel is called Bluefern Lodge Hotel. A 1940s or 1950s vibe of old school magicians would be cool. it should be playful and celebratory.

Target Market(s)

Our in-house hotel guests

Industry/Entity Type

Hotel

Font styles to use
Script

Requirements
Must have
• One of our two logos ,and the desription of the sparkling wine...which is "Special Edition California Brut Alcohol 11.5% by volume

```html
<!DOCTYPE html>
<html lang="en">
<head>
<meta charset="utf-8">
<title>Bluefern Lodge Hotel – Special Edition California Brut Label</title>
<link rel="stylesheet" href="https://fonts.googleapis.com/css2?family=Oswald:wght@500&family=Rubik:wght@400;800&display=swap">
<style>
  :root {
    --teal-deep: #03606e;
    --teal-ink: #0b5866;
    --mint: #a9d6d0;
    --mint-light: #c6e6e1;
    --cream: #f3f1ec;
    --gold: #e9b877;
    --page: #ffffff;
  }
  * { margin: 0; padding: 0; box-sizing: border-box; }
  html, body {
    width: 1084px;
    height: 1200px;
    overflow: hidden;
    background: var(--page);
  }
  .canvas {
    position: relative;
    width: 1084px;
    height: 1200px;
  }
  .wine-label {
    position: absolute;
    left: 92px;
    top: 160px;
    width: 900px;
    height: 880px;
    background: var(--mint);
    overflow: hidden;
  }
  .wine-label__art {
    position: absolute;
    inset: 0;
    width: 900px;
    height: 880px;
  }
  .brand-name {
    position: absolute;
    left: 180px;
    width: 540px;
    top: 355px;
    text-align: center;
    font-family: "Rubik", sans-serif;
    font-weight: 800;
    font-size: 62px;
    line-height: 1.02;
    letter-spacing: 2px;
    color: var(--teal-ink);
    text-transform: uppercase;
  }
  .wine-description {
    position: absolute;
    left: 0;
    width: 900px;
    top: 808px;
    text-align: center;
    color: var(--teal-ink);
  }
  .wine-description__name {
    font-family: "Oswald", sans-serif;
    font-weight: 500;
    font-size: 27px;
    letter-spacing: 0.5px;
    text-transform: uppercase;
    line-height: 1.1;
  }
  .wine-description__abv {
    font-family: "Rubik", sans-serif;
    font-weight: 400;
    font-size: 20px;
    line-height: 1.3;
  }
</style>
</head>
<body>
<main class="canvas">
  <section class="wine-label">
    <svg class="wine-label__art" viewBox="0 0 900 880" xmlns="http://www.w3.org/2000/svg" aria-hidden="true">
      <!-- upper deep teal field -->
      <path d="M0 0 H900 V560 Q860 560 820 575 L450 790 L80 575 Q40 560 0 560 Z" fill="var(--teal-deep)"/>

      <!-- side stripes -->
      <g class="side-stripes" stroke="var(--mint-light)" stroke-width="10">
        <line x1="0" y1="300" x2="140" y2="300"/>
        <line x1="0" y1="335" x2="140" y2="335"/>
        <line x1="0" y1="370" x2="140" y2="370"/>
        <line x1="0" y1="405" x2="140" y2="405"/>
        <line x1="0" y1="440" x2="140" y2="440"/>
        <line x1="0" y1="475" x2="140" y2="475"/>
        <line x1="760" y1="300" x2="900" y2="300"/>
        <line x1="760" y1="335" x2="900" y2="335"/>
        <line x1="760" y1="370" x2="900" y2="370"/>
        <line x1="760" y1="405" x2="900" y2="405"/>
        <line x1="760" y1="440" x2="900" y2="440"/>
        <line x1="760" y1="475" x2="900" y2="475"/>
      </g>
      <g class="side-bands" fill="none" stroke="var(--mint-light)" stroke-width="10">
        <path d="M0 515 Q70 515 125 540"/>
        <path d="M900 515 Q830 515 775 540"/>
      </g>

      <!-- shield: outer ring, mint border, cream field -->
      <path class="shield-outline" d="M112 240 Q112 148 210 148 H690 Q788 148 788 240 V560 Q788 604 750 626 L450 812 L150 626 Q112 604 112 560 Z" fill="var(--teal-deep)"/>
      <path class="shield-border" d="M128 246 Q128 164 216 164 H684 Q772 164 772 246 V556 Q772 594 738 614 L450 794 L162 614 Q128 594 128 556 Z" fill="var(--mint)"/>
      <path class="shield-field" d="M158 256 Q158 192 226 192 H674 Q742 192 742 256 V548 Q742 580 714 596 L450 760 L186 596 Q158 580 158 548 Z" fill="var(--cream)"/>
    </svg>

    <svg style="position:absolute;left:343px;top:218px" width="214" height="42" viewBox="0 0 214 42" role="img" aria-label="Gold scroll flourish ornament">
      <rect width="214" height="42" rx="21" fill="var(--gold)" opacity="0.55"/>
    </svg>

    <div class="brand-name">Bluefern<br>Lodge<br>Hotel</div>

    <svg style="position:absolute;left:390px;top:672px" width="120" height="34" viewBox="0 0 120 34" role="img" aria-label="Small gold flourish ornament">
      <rect width="120" height="34" rx="17" fill="var(--gold)" opacity="0.55"/>
    </svg>

    <div class="wine-description">
      <p class="wine-description__name">Special Edition California Brut</p>
      <p class="wine-description__abv">Alcohol 11.5% by volume</p>
    </div>
  </section>
</main>
</body>
</html>
```